ALL TEXT Social Media Graphics

We are looking for a series of social media graphics for Instagram (new size: 4:5 (1080 x 1350 pixels) ratio that are ALL TEXT. We want the following quotes below on each graphic; one quote per graphic. AND, In very small letters at the bottom of each graphic, add @PaulaWrenLive
The look and feel of these graphics should be complimentary to the color palette attached below; but keep them simple. But the design is up to you; at the end of this document, I provided various samples of all text graphics that I like as examples.
The Quotes are in the attached WORD document
women trying to lose weight

```html
<!DOCTYPE html>
<html lang="en">
<head>
<meta charset="utf-8">
<title>Golden Summer Slimdown – Social Graphics</title>
<link rel="stylesheet" href="https://fonts.googleapis.com/css2?family=Roboto+Serif:opsz,wght@8..144,300;8..144,600&family=Barlow:ital,wght@0,300;0,400;0,600;1,300&family=Barlow+Condensed:wght@700&family=Fjalla+One&family=Arimo:wght@700&family=Ubuntu:wght@500;700&display=swap">
<style>
  :root {
    --backdrop: #b3b3b3;
    --card: #ffffff;
    --pink: #ee5e95;
    --magenta: #b3205b;
    --slate: #5e6a80;
    --blush: #f7c3da;
    --ink: #333333;
  }
  * { margin: 0; padding: 0; box-sizing: border-box; }
  html, body { width: 991px; height: 1200px; overflow: hidden; background: var(--backdrop); }
  .canvas { position: relative; width: 991px; height: 1200px; }
  .post {
    position: absolute; width: 437px; height: 546px; background: var(--card);
  }
  .post--one { left: 30px; top: 29px; }
  .post--two { left: 518px; top: 29px; background: linear-gradient(to bottom, var(--card) 44%, var(--blush) 100%); }
  .post--three { left: 30px; top: 620px; background: linear-gradient(to bottom, var(--blush) 0%, var(--card) 41%); }
  .post--four { left: 516px; top: 624px; }

  .block { position: absolute; }
  .block--left { left: 47px; }
  .block--right { right: 46px; text-align: right; }

  .serif { font-family: "Roboto Serif", Georgia, serif; font-weight: 300; }
  .serif strong { font-weight: 600; }
  .light { font-family: "Barlow", Helvetica, sans-serif; font-weight: 300; }
  .light strong { font-weight: 600; }
  .condensed { font-family: "Barlow Condensed", "Arial Narrow", sans-serif; font-weight: 700; text-transform: uppercase; }

  .pink { color: var(--pink); }
  .magenta { color: var(--magenta); }
  .slate { color: var(--slate); }

  .handle {
    position: absolute; right: 47px; top: 494px;
    font-family: "Barlow", Helvetica, sans-serif; font-style: italic; font-weight: 300;
    font-size: 13px; color: var(--ink);
  }

  /* Post one */
  .one-headline { top: 74px; font-size: 30px; line-height: 34px; }
  .one-support { top: 217px; font-size: 23px; line-height: 29px; letter-spacing: 0.3px; }
  .one-cta { top: 320px; font-family: "Arimo", Arial, sans-serif; font-weight: 700; font-size: 22px; line-height: 29px; }

  /* Post two */
  .two-headline { top: 77px; font-size: 34px; line-height: 38px; }
  .two-support { top: 254px; font-size: 23px; line-height: 29px; }
  .two-cta { top: 345px; font-family: "Fjalla One", Impact, sans-serif; font-size: 31px; line-height: 34px; color: var(--magenta); }

  /* Post three */
  .three-headline { top: 76px; font-size: 34px; line-height: 38px; }
  .three-support { top: 222px; right: 52px; font-family: "Barlow", Helvetica, sans-serif; font-weight: 400; font-size: 27px; line-height: 34px; }
  .three-support strong { font-weight: 600; }
  .three-support .shift { margin-right: -6px; display: inline-block; }
  .three-cta { top: 361px; left: 0; width: 437px; text-align: center; font-size: 30px; line-height: 33px; }

  /* Post four */
  .four-headline { top: 63px; left: 48px; font-size: 31px; line-height: 39px; }
  .four-plan { top: 240px; left: 0; width: 437px; text-align: center; font-family: "Ubuntu", sans-serif; font-weight: 700; font-size: 27px; }
  .four-cta { top: 335px; font-family: "Ubuntu", sans-serif; font-weight: 500; font-size: 27px; line-height: 34px; }
</style>
</head>
<body>
<main class="canvas">

  <section class="post post--one">
    <p class="block block--left one-headline serif pink">You can absolutely<br>be down <strong>20–30 pounds</strong><br>by end of summer.</p>
    <p class="block block--left one-support light slate">All it takes is the right plan<br>and you’ve found it.</p>
    <p class="block block--left one-cta pink">Comment “Golden”<br>for the Golden<br>Summer Slimdown!</p>
    <p class="handle">@PaulaWrenLive</p>
  </section>

  <section class="post post--two">
    <h2 class="block block--left two-headline condensed"><span class="magenta">You don’t need<br>another diet</span><br><span class="pink">You need a system<br>that works.</span></h2>
    <p class="block block--left two-support light pink">Drop <strong>30 pounds</strong> with<br>the Golden Summer Slimdown.</p>
    <p class="block block--left two-cta">Comment “Summer”<br>to start now.</p>
    <p class="handle">@PaulaWrenLive</p>
  </section>

  <section class="post post--three">
    <h2 class="block block--right three-headline condensed"><span class="magenta">This summer ain’t over</span><br><span class="pink">and neither are your<br>body goals.</span></h2>
    <p class="block block--right three-support slate"><strong>Drop 30 pounds</strong><br>with the Golden<br><span class="shift">Summer Slimdown.</span></p>
    <p class="block three-cta serif pink">Comment “Golden”<br>to get the plan.</p>
    <p class="handle">@PaulaWrenLive</p>
  </section>

  <section class="post post--four">
    <h2 class="block four-headline serif pink">If your goal is a<br>tiny waist, flat belly,<br>and <strong>30 pounds down</strong></h2>
    <p class="block four-plan magenta">this is the plan</p>
    <p class="block block--right four-cta pink">Comment “Summer”<br>to join the Golden<br>Summer Slimdown!</p>
    <p class="handle">@PaulaWrenLive</p>
  </section>

</main>
</body>
</html>
```